Web Design Project

Psychotherapy and Counselling Practice needs a landing page web design.

My business "Larkspur Advisory" specialises in the treatment of Anxiety and Depression with a holistic approach, endeavouring to unlock the key that holds us to ransom in a life that is imbalanced, frustrating, and ultimately of our own making due to our own perceptions and behaviours.

There is much that impacts us which we cannot change, but we are always in control of how we think, and how we frame our experiences.....learning to challenge those thoughts and behaviours that are destructive and disempowering opens up a world of joyful possibility. Life is about making choices, learn to make wiser and healthier choices.......

Larkspur Advisory has a client base of individual clients but will seek to expand to offer services to the Corporate world by offering an adjunct to employers for established "Wellness Programs".

Larkspur Advisory is a highly professional, ethically bound business, with the needs of the client at the forefront of all we do.

Larkspur Advisory wishes to avoid the usual "jargon driven" psychobabble offered on many counselling web pages. It aims to be stylishly presented, clean in look and with as few "words" as possible and a largely white background (faster loading and more powerful impact of what is stated), those words contained in the webpage should be meaningful, persuasive and have an impact simply at glance. Larkspur does not want , or expect, those prospective clients in need of support , to be reading through volumes of industry driven cliches.

At this point Larkspur is just looking for a high quality landing page. However in time this will likely expand to include other sections such as case studies, video content etc.

Target Market(s)

Those in need of emotional support, suffering mental health issues, and those simply wanting to become self aware supported by a mindful therapist.

Industry/Entity Type

Industry

Requirements
Must have
• The design must incorporate the Larkspur logo and colour schemes found on the attached files.

```html
<!DOCTYPE html>
<html lang="en">
<head>
<meta charset="utf-8">
<title>Larkspur Advisory</title>
<link href="https://fonts.googleapis.com/css2?family=Open+Sans:ital,wght@0,300;0,400;0,600;1,400&display=swap" rel="stylesheet">
<style>
:root{
  --green:#8bb21f;
  --green-dark:#6f9414;
  --sky:#1f74c8;
  --sky-light:#8cc6ef;
  --ink:#3a3a3a;
  --muted:#777;
  --line:#cfcfcf;
  --band:#eeeeee;
  --footer:#5b5b5b;
  --footer-text:#e6e6e6;
  --white:#ffffff;
}
*{box-sizing:border-box;margin:0;padding:0}
html,body{width:769px;height:1200px;overflow:hidden;background:var(--white)}
body{font-family:"Open Sans",Arial,sans-serif;color:var(--ink);position:relative}

.site-header{position:absolute;top:0;left:0;width:769px;height:92px}
.brand{position:absolute;left:48px;top:40px;font-size:20px;font-weight:400;letter-spacing:1px;color:var(--green)}
.main-nav{position:absolute;left:290px;top:50px;display:flex;gap:30px}
.main-nav a{font-size:10px;color:var(--muted);text-decoration:none;letter-spacing:.5px}
.social{position:absolute;right:55px;top:14px;display:flex;gap:8px}
.social span{width:18px;height:18px;border-radius:50%;background:var(--green)}

.hero{position:absolute;top:92px;left:0;width:769px;height:300px}
.hero-photo{position:absolute;inset:0;background:linear-gradient(180deg,var(--sky) 0%,#3b8fd8 55%,var(--sky-light) 100%)}
.hero-wave{position:absolute;left:0;bottom:0;width:769px;height:120px}
.hero-tagline{position:absolute;left:98px;top:188px;color:var(--white);font-size:15px;line-height:21px;font-weight:300;white-space:nowrap}
.hero-tagline strong{font-size:20px;font-weight:400}
.hero-tagline em{font-style:normal;color:#dff3a0;font-weight:400}

.intro{position:absolute;top:440px;left:0;width:769px;text-align:center}
.intro-map{position:absolute;left:205px;top:-10px;width:360px;height:200px;background:radial-gradient(ellipse at center,#e9eee0 0%,rgba(255,255,255,0) 70%)}
.intro h1{position:relative;font-size:20px;font-weight:400;line-height:26px;color:var(--ink);letter-spacing:.5px}
.intro p{position:relative;margin:20px auto 0;width:600px;font-size:15px;line-height:20px;color:var(--muted)}

.contact-form{position:absolute;top:640px;left:0;width:769px}
.contact-form h2{text-align:center;font-size:20px;font-weight:400;letter-spacing:.5px}
.field{position:absolute;border:1px solid var(--line);border-radius:4px;font-size:13px;color:#999;padding:6px 10px}
.field-name{left:78px;top:58px;width:255px;height:30px}
.field-email{left:78px;top:103px;width:255px;height:30px}
.field-message{left:365px;top:58px;width:325px;height:80px}
.btn-help{position:absolute;left:482px;top:172px;width:210px;height:42px;border-radius:6px;background:var(--green);color:var(--white);font-size:15px;letter-spacing:.5px;display:flex;align-items:center;justify-content:center}

.testimonial{position:absolute;top:908px;left:0;width:769px;height:150px;background:var(--band)}
.portrait{position:absolute;left:80px;top:28px;width:92px;height:92px;border-radius:50%;background:linear-gradient(160deg,#c9b8a8,#6b5548);border:3px solid var(--white)}
.quote{position:absolute;left:210px;top:20px;width:478px;height:110px;background:var(--white);border-radius:4px;padding:16px 24px 0 48px}
.quote-mark{position:absolute;left:16px;top:4px;font-size:40px;color:#bdbdbd}
.quote p{font-size:9.5px;line-height:14px;color:var(--muted);font-style:italic}
.quote cite{display:block;margin-top:10px;font-size:9.5px;font-style:normal;color:var(--muted)}
.quote cite b{color:var(--ink);font-weight:600}

.site-footer{position:absolute;top:1058px;left:0;width:769px;height:142px;background:var(--footer);color:var(--footer-text)}
.footer-col{position:absolute;top:18px}
.footer-col h3{font-size:13px;font-weight:400;margin-bottom:6px}
.footer-col li{list-style:none;font-size:8.5px;line-height:12px}
.col-links{left:78px}
.col-tweets{left:196px;width:170px}
.col-tweets p{font-size:8.5px;line-height:12px}
.col-contact{left:412px;width:190px}
.col-contact dl{display:grid;grid-template-columns:52px 1fr;font-size:8.5px;line-height:12px}
.footer-brand{position:absolute;left:622px;top:82px;font-size:16px;letter-spacing:1px;color:var(--white)}
</style>
</head>
<body>
<header class="site-header">
  <div class="brand">LARKSPUR</div>
  <nav class="main-nav"><a>HOME</a><a>ABOUT</a><a>SERVICES</a><a>TESTIMONIALS</a><a>CONTACT</a></nav>
  <div class="social"><span></span><span></span><span></span></div>
</header>

<section class="hero">
  <div class="hero-photo" role="img" aria-label="Woman leaping joyfully under a bright blue sky holding a flowing green scarf"></div>
  <svg class="hero-wave" viewBox="0 0 769 120" preserveAspectRatio="none">
    <path d="M0 120 L0 104 C250 74 500 58 769 62 L769 120 Z" fill="#ffffff"/>
    <path d="M0 104 C250 74 500 58 769 62" fill="none" stroke="#8bb21f" stroke-width="6"/>
    <path d="M0 97 C250 67 500 51 769 55" fill="none" stroke="#ffffff" stroke-width="2" opacity=".7"/>
  </svg>
  <div class="hero-tagline"><strong>Life</strong> is to short<br>to live in <em>unhappy</em> life...</div>
</section>

<section class="intro">
  <div class="intro-map" role="img" aria-label="Faint world map"></div>
  <h1>WE ARE HERE TO HELP SUPPORT ANYONE WHO WISHES<br>TO LIVE THE LIFE THAT IS TRUEST TO WHO THEY ARE</h1>
  <p>Research shows that more than half of the people around the world are not satisfied and happy with their life, we try to help people to find their happiness and make their life worth living.</p>
</section>

<section class="contact-form">
  <h2>NEED SOMEONE TO TALK TO?</h2>
  <div class="field field-name">name</div>
  <div class="field field-email">e-mail</div>
  <div class="field field-message">messages</div>
  <div class="btn-help">ASK FOR HELP</div>
</section>

<section class="testimonial">
  <div class="portrait" role="img" aria-label="Portrait of a client"></div>
  <blockquote class="quote">
    <span class="quote-mark">&ldquo;</span>
    <p>Talking things through here helped me see my own patterns clearly. I learned to pause, question my thoughts and choose calmer responses. Each session felt warm, honest and practical, and I now face work and home with far more balance and confidence than before.</p>
    <cite><b>Clara,</b> Director of Northfield Group</cite>
  </blockquote>
</section>

<footer class="site-footer">
  <div class="footer-col col-links">
    <h3>Useful Links</h3>
    <ul><li>About Us</li><li>Services</li><li>Sessions</li><li>Support</li><li>Contact Us</li></ul>
  </div>
  <div class="footer-col col-tweets">
    <h3>Latest Tweets</h3>
    <p>Larkspur: Small daily choices shape a calmer mind, start with one kind thought today. 2 hours ago</p>
    <p>Larkspur: New group sessions open next month for workplace wellness. 1 day ago</p>
  </div>
  <div class="footer-col col-contact">
    <h3>Contact Us</h3>
    <dl>
      <dt>Phone:</dt><dd>+00 555 0199</dd>
      <dt>Fax:</dt><dd>+00 555 0188</dd>
      <dt>Email:</dt><dd>hello@larkspur.example</dd>
      <dt>Address:</dt><dd>12 Meadow Lane, Fernvale City</dd>
    </dl>
  </div>
  <div class="footer-brand">LARKSPUR</div>
</footer>
</body>
</html>
```